Mobile Friendly Lead Generation Landing Page

We are a web marketing company that specialized in web lead generation. Recently we have started buying media from mobile devices and we need a mobile interface(landing page) where we can collect user data in an effective manner.

Our current mobile landing page is:
http://www.pathwaylocate.example.com/lp13d/index.aspx?a=true&source=591483
Through this you can see what the steps/questions users need to answer to get matched to a school. We need the design for the whole process.

We are pretty open for design ideas and our goal is to make this mobile optimized landing page have the look and feel of an app...but not an app.
There are several questions in the process but we are open to changing the way they are presented. As in, you can have one question at a time or a few.
The goal is to make this EXTREMELY EASY for users to interact with.

One example that we have liked is:
http://tutorhubnet.example.com/schools/72615-page1.thub (please note that this opens only on mobile devices)

Some of these screenshots are attached.

Our web form looks like this:
http://www.pathwaylocate.example.com/lp88/index.aspx?a=true

```html
<!DOCTYPE html>
<html lang="en">
<head>
<meta charset="utf-8">
<title>Two Minute Form – Personal Details</title>
<link rel="stylesheet" href="https://fonts.googleapis.com/css2?family=Open+Sans:ital,wght@0,300;0,400;0,600;0,700;1,300;1,400;1,700&display=swap">
<style>
  :root {
    --page-bg: #e6e7e9;
    --screen-bg: #eceef0;
    --navy-dark: #1b2b3f;
    --navy: #26394f;
    --navy-light: #34496a;
    --segment-empty: #3b5170;
    --green: #6cc24a;
    --green-dark: #4ea22c;
    --green-light: #8fd66c;
    --card: #f9f9fa;
    --field: #efefef;
    --field-edge: #e2e2e2;
    --label: #8f959b;
    --heading: #7d848b;
    --header-text: #d9e1ea;
    --muted-header: #7f93ab;
    --white: #ffffff;
  }
  * { box-sizing: border-box; margin: 0; padding: 0; }
  html, body {
    width: 1190px;
    height: 1200px;
    overflow: hidden;
    background: var(--page-bg);
    font-family: "Open Sans", Arial, sans-serif;
  }
  .screen {
    position: absolute;
    left: 275px;
    top: 32px;
    width: 640px;
    height: 1136px;
    background: var(--screen-bg);
    overflow: hidden;
  }
  /* status bar */
  .status-bar {
    height: 40px;
    background: var(--navy-dark);
    color: var(--white);
    display: flex;
    align-items: center;
    justify-content: space-between;
    padding: 0 14px;
    font-size: 22px;
    font-weight: 700;
    position: relative;
  }
  .status-carrier, .status-right { display: flex; align-items: center; gap: 8px; }
  .status-time {
    position: absolute;
    left: 50%;
    transform: translateX(-50%);
  }
  /* header */
  .form-header {
    height: 260px;
    background: linear-gradient(180deg, var(--navy-light) 0%, var(--navy) 45%, var(--navy-dark) 100%);
    position: relative;
    text-align: center;
  }
  .nav-button {
    position: absolute;
    top: 32px;
    width: 34px;
    height: 34px;
  }
  .nav-back { left: 22px; }
  .nav-forward { right: 22px; }
  .form-title {
    padding-top: 34px;
    font-size: 24px;
    font-weight: 400;
    color: var(--header-text);
  }
  .form-title strong { font-weight: 700; color: var(--white); }
  .progress-track {
    display: flex;
    justify-content: center;
    gap: 8px;
    margin-top: 42px;
  }
  .progress-segment {
    width: 116px;
    height: 26px;
    background: var(--segment-empty);
    box-shadow: inset 0 1px 2px rgba(0,0,0,.25);
  }
  .progress-segment.is-done {
    background: linear-gradient(180deg, var(--green-light), var(--green) 55%, var(--green-dark));
  }
  .progress-caption {
    margin-top: 10px;
    font-size: 15px;
    font-style: italic;
    font-weight: 300;
    color: var(--muted-header);
  }
  /* card */
  .details-card {
    position: absolute;
    left: 24px;
    right: 24px;
    top: 268px;
    bottom: 44px;
    background: var(--card);
    box-shadow: 0 1px 3px rgba(0,0,0,.08);
    padding: 70px 62px 0;
  }
  .help-icon {
    position: absolute;
    top: 18px;
    right: 18px;
    width: 30px;
    height: 30px;
  }
  .card-heading {
    text-align: center;
    font-size: 32px;
    line-height: 44px;
    font-weight: 300;
    font-style: italic;
    color: var(--heading);
    margin-bottom: 36px;
  }
  .field { margin-bottom: 22px; }
  .field-label {
    display: block;
    font-size: 17px;
    line-height: 23px;
    font-style: italic;
    font-weight: 300;
    color: var(--label);
    margin: 0 0 8px 26px;
  }
  .field-input {
    height: 54px;
    background: var(--field);
    border-bottom: 2px solid var(--field-edge);
    position: relative;
  }
  .select-arrow {
    position: absolute;
    right: 16px;
    top: 20px;
  }
  .phone-group { display: flex; gap: 6px; }
  .phone-group .field-input:nth-child(1) { flex: 0 0 120px; }
  .phone-group .field-input:nth-child(2) { flex: 0 0 132px; }
  .phone-group .field-input:nth-child(3) { flex: 1; }
  .next-button {
    margin-top: 38px;
    height: 70px;
    background: linear-gradient(180deg, var(--green-light) 0%, var(--green) 50%, var(--green-dark) 100%);
    color: var(--white);
    font-size: 30px;
    font-weight: 700;
    font-style: italic;
    display: flex;
    align-items: center;
    justify-content: center;
    gap: 20px;
    box-shadow: 0 2px 3px rgba(0,0,0,.15);
  }
</style>
</head>
<body>
  <main class="screen">
    <div class="status-bar">
      <div class="status-carrier">
        <svg width="30" height="16" viewBox="0 0 30 16" aria-hidden="true">
          <rect x="0" y="11" width="4" height="5" fill="#fff"/>
          <rect x="6" y="8" width="4" height="8" fill="#fff"/>
          <rect x="12" y="5" width="4" height="11" fill="#fff"/>
          <rect x="18" y="2" width="4" height="14" fill="#fff"/>
          <rect x="24" y="0" width="4" height="16" fill="#fff" opacity=".5"/>
        </svg>
        <span>LUMA</span>
      </div>
      <span class="status-time">10:35 AM</span>
      <div class="status-right">
        <svg width="18" height="18" viewBox="0 0 18 18" aria-hidden="true">
          <circle cx="9" cy="9" r="8" fill="#fff"/>
          <path d="M9 4v5l3 2" stroke="#1b2b3f" stroke-width="2" fill="none"/>
        </svg>
        <span>65%</span>
        <svg width="40" height="18" viewBox="0 0 40 18" aria-hidden="true">
          <rect x="1" y="1" width="34" height="16" rx="2" fill="none" stroke="#fff" stroke-width="2"/>
          <rect x="4" y="4" width="20" height="10" fill="#fff"/>
          <rect x="36" y="6" width="3" height="6" fill="#fff"/>
        </svg>
      </div>
    </div>

    <header class="form-header">
      <svg class="nav-button nav-back" viewBox="0 0 34 34" aria-label="Back" role="img">
        <circle cx="17" cy="17" r="15" fill="none" stroke="#8ea2bb" stroke-width="2"/>
        <path d="M24 17H11M16 11l-6 6 6 6" stroke="#8ea2bb" stroke-width="2.4" fill="none"/>
      </svg>
      <h1 class="form-title">Fill out our <strong>2 MINUTE</strong> form!</h1>
      <svg class="nav-button nav-forward" viewBox="0 0 34 34" aria-label="Forward" role="img">
        <circle cx="17" cy="17" r="15" fill="none" stroke="#8ea2bb" stroke-width="2"/>
        <path d="M10 17h13M18 11l6 6-6 6" stroke="#8ea2bb" stroke-width="2.4" fill="none"/>
      </svg>
      <div class="progress-track">
        <div class="progress-segment is-done"></div>
        <div class="progress-segment is-done"></div>
        <div class="progress-segment"></div>
        <div class="progress-segment"></div>
      </div>
      <p class="progress-caption">progress : 76% completed</p>
    </header>

    <section class="details-card">
      <svg class="help-icon" viewBox="0 0 30 30" aria-label="Help" role="img">
        <circle cx="15" cy="15" r="13" fill="none" stroke="#c4c7cb" stroke-width="2"/>
        <text x="15" y="21" text-anchor="middle" font-family="Open Sans, sans-serif" font-size="17" fill="#b8bcc1">?</text>
      </svg>
      <h2 class="card-heading">Personal details :</h2>

      <div class="field">
        <span class="field-label">Salutation :</span>
        <div class="field-input">
          <svg class="select-arrow" width="16" height="12" viewBox="0 0 16 12" aria-hidden="true">
            <path d="M0 0h16L8 12z" fill="#9aa0a6"/>
          </svg>
        </div>
      </div>
      <div class="field">
        <span class="field-label">First Name :</span>
        <div class="field-input"></div>
      </div>
      <div class="field">
        <span class="field-label">Last Name :</span>
        <div class="field-input"></div>
      </div>
      <div class="field">
        <span class="field-label">Email :</span>
        <div class="field-input"></div>
      </div>
      <div class="field">
        <span class="field-label">Phone :</span>
        <div class="phone-group">
          <div class="field-input"></div>
          <div class="field-input"></div>
          <div class="field-input"></div>
        </div>
      </div>

      <div class="next-button">
        <span>Next</span>
        <svg width="12" height="20" viewBox="0 0 12 20" aria-hidden="true">
          <path d="M2 2l8 8-8 8" stroke="#fff" stroke-width="3" fill="none"/>
        </svg>
      </div>
    </section>
  </main>
</body>
</html>
```